Personal Tax Specialists Banner

We need banner adverts for a personal tax firm. We specialise in Luxembourg, US and UK personal taxation. The banner should be modern, cool, simple and illustrated.

Banner should highlight "Personal Taxation Specialists" and the countries that we specialise in, "Luxembourg", "US" and "UK".

Target Market(s)

Individuals looking for assistance with tax return preparation.

Industry/Entity Type

Finance And Accounting

Colors

Designer to choose colors to be used in the design.

Requirements
Must have
• Output in GIF.
• The main banner size is 980 x 120 and some smaller square banners (300 x 300)
• Button to link back to website www.corvinfiling.com
Nice to have
• We would like an illustrated design if possible.

```html
<!DOCTYPE html>
<html lang="en">
<head>
<meta charset="utf-8">
<title>Corvin Tax &amp; Filing – 980 x 120 Banner</title>
<link rel="stylesheet" href="https://fonts.googleapis.com/css2?family=Montserrat:wght@400;500;700&display=swap">
<style>
  :root {
    --paper: #ffffff;
    --ink: #111111;
    --heading-grey: #9a9a9a;
    --maroon: #7a0534;
    --photo-light: #f3f1ef;
    --photo-mid: #dcdcdc;
    --photo-warm: #ece3dc;
    --sub-ink: #222222;
  }
  * { margin: 0; padding: 0; box-sizing: border-box; }
  html, body { width: 1200px; height: 1200px; overflow: hidden; background: var(--paper); }
  body { position: relative; font-family: "Montserrat", sans-serif; color: var(--ink); }

  .sheet-title {
    position: absolute; left: 54px; top: 48px;
    font-size: 60px; font-weight: 700; color: var(--heading-grey); letter-spacing: 0.5px;
  }
  .photo-credit {
    position: absolute; left: 54px; top: 145px;
    font-size: 27px; font-weight: 500; line-height: 41px;
  }
  .note {
    position: absolute; width: 300px; text-align: center;
    font-size: 19px; font-weight: 500; line-height: 29.6px; letter-spacing: 0.3px;
  }
  .note p + p { margin-top: 20px; }
  .note--intro { left: 860px; top: 113px; }

  .banner {
    position: absolute; left: 11px; width: 1174px; height: 144px; overflow: hidden;
  }
  .banner--personal { top: 298px; }
  .banner--services { top: 771px; }

  .banner__photo { position: absolute; inset: 0; }
  .banner--personal .banner__photo {
    background: linear-gradient(90deg, var(--photo-light) 0%, var(--photo-warm) 30%, var(--photo-light) 55%, var(--photo-mid) 75%, #e6e9ec 100%);
  }
  .banner--services .banner__photo {
    background: linear-gradient(90deg, var(--photo-light) 0%, #e9e9e9 25%, var(--photo-light) 55%, var(--photo-warm) 80%, var(--photo-mid) 100%);
  }

  .brand { position: absolute; left: 29px; top: 30px; display: flex; align-items: center; gap: 16px; }
  .brand__mark { width: 80px; height: 80px; }
  .brand__name { color: var(--maroon); font-weight: 500; line-height: 1; }
  .brand__name-main { display: block; font-size: 44px; letter-spacing: 0.5px; }
  .brand__name-sub { display: block; font-size: 17px; margin-top: 6px; letter-spacing: 0.2px; }

  .message { position: absolute; left: 346px; width: 500px; top: 38px; text-align: center; }
  .message__headline { font-size: 32px; font-weight: 700; color: var(--ink); white-space: nowrap; }
  .banner--services .message__headline { font-size: 27.5px; padding-top: 4px; }
  .message__regions { font-size: 16px; font-weight: 500; color: var(--sub-ink); margin-top: 4px; }
  .message__rule { width: 74px; height: 2.5px; background: var(--maroon); margin: 13px auto 0; }

  .cta {
    position: absolute; left: 912px; top: 43px; width: 230px; height: 61px;
    border-radius: 16px; background: var(--maroon); color: #fff;
    display: flex; align-items: center; justify-content: center;
    font-size: 23px; font-weight: 700; letter-spacing: 0.5px; text-decoration: none;
  }

  .note--logo-1 { left: 40px; top: 484px; }
  .note--copy-1 { left: 449px; top: 484px; }
  .note--cta-1 { left: 860px; top: 488px; }
  .note--logo-2 { left: 57px; top: 977px; }
  .note--copy-2 { left: 449px; top: 977px; }
  .note--cta-2 { left: 860px; top: 977px; }
</style>
</head>
<body>
  <h1 class="sheet-title">980 x 120 Banner</h1>
  <p class="photo-credit">*All photography used is license free<br>from: https://www.freefotobank.com/</p>

  <div class="note note--intro">
    <p>The opening statement talks about being Personal - I have used a one-to-one discussion for this as it illustrates working closely with the client.</p>
  </div>

  <section class="banner banner--personal">
    <div class="banner__photo" role="img" aria-label="Faded photo of two people in a one-to-one discussion at a desk"></div>
    <div class="brand">
      <svg class="brand__mark" viewBox="0 0 80 80" aria-hidden="true"><circle cx="40" cy="40" r="38" fill="none" stroke="#9a9a9a" stroke-width="2"/></svg>
      <div class="brand__name"><span class="brand__name-main">CORVIN</span><span class="brand__name-sub">TAX &amp; FILING</span></div>
    </div>
    <div class="message">
      <h2 class="message__headline">Personal Taxation Specialists</h2>
      <p class="message__regions">Specialising in Luxembourg, US and UK</p>
      <div class="message__rule"></div>
    </div>
    <a class="cta" href="https://www.corvinfiling.com">Find out more</a>
  </section>

  <div class="note note--logo-1"><p>Logo to animate in from left Slides in whilst fading in at the same time.</p></div>
  <div class="note note--copy-1"><p>Copy to fade in word by word. Red line to animate in from the central point out.</p></div>
  <div class="note note--cta-1">
    <p>CTA button has placeholder copy - you can suggest this?</p>
    <p>Buttom to animate in from either the right or top/bottom</p>
  </div>

  <section class="banner banner--services">
    <div class="banner__photo" role="img" aria-label="Faded photo of a laptop on a desk and a hand holding a phone"></div>
    <div class="brand">
      <svg class="brand__mark" viewBox="0 0 80 80" aria-hidden="true"><circle cx="40" cy="40" r="38" fill="none" stroke="#9a9a9a" stroke-width="2"/></svg>
      <div class="brand__name"><span class="brand__name-main">CORVIN</span><span class="brand__name-sub">TAX &amp; FILING</span></div>
    </div>
    <div class="message">
      <h2 class="message__headline">Personal, Efficient &amp; Flexible Services</h2>
      <p class="message__regions">Specialising in Luxembourg, US and UK</p>
      <div class="message__rule"></div>
    </div>
    <a class="cta" href="https://www.corvinfiling.com">Find out more</a>
  </section>

  <div class="note note--logo-2"><p>I used this line of copy from your website under your about page. Three key points to get across to potential clients</p></div>
  <div class="note note--copy-2"><p>Copy to fade in word by word. Red line to animate in from the central point out.</p></div>
  <div class="note note--cta-2">
    <p>CTA button has placeholder copy - you can suggest this?</p>
    <p>Buttom to animate in from either the right or top/bottom</p>
  </div>
</body>
</html>
```